we are a small based family business that specialise in 12v led lights for tarvin caravans.
we also sell 12v switches, wire, circuit breakers, dimmers etc but our main line is LEDs.
We would like something that reflects the LED lighting on our cards.
www.reefcrestlamps.example.au is where you can have a look at to get ideas, of our product.
I have attached the logo we generally use on all our shopra listings and is the main header on our website.

Look forward to seeing what your team comes up with.

Business

Tam 0491 738 205
Corrawin Vale QLD 4391

www.reefcrestlamps.example

```html
<!DOCTYPE html>
<html lang="en">
<head>
<meta charset="utf-8">
<title>Reefcrest Lamps – Business Card</title>
<link rel="stylesheet" href="https://fonts.googleapis.com/css2?family=Open+Sans:wght@400;600;700;800&display=swap">
<style>
  :root {
    --backdrop: #4a403b;
    --card-back: #0d0d0e;
    --card-front: #1b1b1c;
    --gloss: #3b3b3e;
    --white: #f4f4f4;
    --red: #c8252c;
    --glow: rgba(200, 37, 44, 0.16);
    --rule: #9a9a9a;
  }
  * { box-sizing: border-box; margin: 0; padding: 0; }
  html, body {
    width: 1200px;
    height: 795px;
    overflow: hidden;
  }
  body {
    background: var(--backdrop);
    font-family: "Open Sans", Arial, sans-serif;
    position: relative;
  }
  .card {
    position: absolute;
    top: 237px;
    width: 540px;
    height: 320px;
    border-radius: 3px;
    overflow: hidden;
    box-shadow: 0 10px 30px rgba(0, 0, 0, 0.45);
  }
  .card--back {
    left: 40px;
    background:
      radial-gradient(ellipse 60% 45% at 55% 50%, rgba(255, 255, 255, 0.05), transparent 70%),
      var(--card-back);
    display: flex;
    align-items: center;
    justify-content: center;
  }
  .card--front {
    left: 620px;
    background:
      radial-gradient(ellipse 55% 60% at 80% 20%, var(--glow), transparent 70%),
      radial-gradient(ellipse 40% 40% at 20% 90%, rgba(200, 37, 44, 0.07), transparent 70%),
      var(--card-front);
  }
  .brand-name {
    font-weight: 800;
    text-transform: uppercase;
    line-height: 0.95;
    letter-spacing: 0.5px;
  }
  .card--back .brand-name {
    color: var(--gloss);
    font-size: 64px;
    text-align: left;
  }
  .card--front .brand-name {
    position: absolute;
    top: 40px;
    left: 140px;
    color: var(--white);
    font-size: 60px;
  }
  .identity {
    position: absolute;
    top: 186px;
    right: 286px;
    text-align: right;
    color: var(--white);
    font-size: 14px;
    line-height: 1.5;
  }
  .identity__name {
    color: var(--red);
    font-weight: 700;
    font-size: 24px;
    line-height: 1.2;
    margin-bottom: 4px;
  }
  .divider {
    position: absolute;
    left: 270px;
    top: 196px;
    width: 1px;
    height: 96px;
    background: var(--rule);
  }
  .contacts {
    position: absolute;
    left: 286px;
    top: 192px;
    list-style: none;
    color: var(--white);
    font-size: 14px;
  }
  .contacts li {
    display: flex;
    align-items: center;
    gap: 8px;
    height: 25px;
    white-space: nowrap;
  }
  .contacts svg {
    width: 12px;
    height: 12px;
    fill: var(--red);
    flex: none;
  }
</style>
</head>
<body>
  <section class="card card--back" aria-label="Card back">
    <span class="brand-name">Reefcrest<br>Lamps</span>
  </section>

  <section class="card card--front" aria-label="Card front">
    <span class="brand-name">Reefcrest<br>Lamps</span>

    <div class="identity">
      <p class="identity__name">Tam</p>
      <p>Managing Member</p>
      <p>Corrawin Vale</p>
      <p>QLD 4391</p>
    </div>

    <div class="divider"></div>

    <ul class="contacts">
      <li>
        <svg viewBox="0 0 12 12" aria-hidden="true"><path d="M3 0h6a1 1 0 0 1 1 1v10a1 1 0 0 1-1 1H3a1 1 0 0 1-1-1V1a1 1 0 0 1 1-1zm0.5 1.5v7.5h5V1.5z"/></svg>
        0491 738 205
      </li>
      <li>
        <svg viewBox="0 0 12 12" aria-hidden="true"><path d="M0 2h12v1L6 7 0 3z"/><path d="M0 4.2l6 4 6-4V10H0z"/></svg>
        tam@reefcrestlamps.example
      </li>
      <li>
        <svg viewBox="0 0 12 12" aria-hidden="true"><circle cx="6" cy="6" r="5.5"/><path d="M0.5 6h11M6 0.5c-3 3-3 8 0 11M6 0.5c3 3 3 8 0 11" stroke="#1b1b1c" stroke-width="0.9" fill="none"/></svg>
        www.reefcrestlamps.example
      </li>
      <li>
        <svg viewBox="0 0 12 12" aria-hidden="true"><circle cx="6" cy="6" r="5.5"/><path d="M0.5 6h11M6 0.5c-3 3-3 8 0 11M6 0.5c3 3 3 8 0 11" stroke="#1b1b1c" stroke-width="0.9" fill="none"/></svg>
        www.reefcrestlamps.example.au
      </li>
    </ul>
  </section>
</body>
</html>
```